Coral Meadow Select Bird Nest needs a sticker design

We need a sticker design to be pasted on the top of our current acrylic box packaging. The sticker design can be derived from our website design at coral-meadow.sg. The sticker design should show some characteristic of 60% Indonesia (where the edible bird nest is harvested) and 40% Singapore (where the edible bird nest is sold). The sticker design should incorporate chinese word for edible bird nest: 燕窩. Thank you for your kind consideration
Target Market(s)
Singaporean chinese customers
Industry/Entity Type
Food Production
Font styles to use
Requirements
Must have
- - Coral Meadow Bird Nest logo attached (please help to delete the chinese wording inside the logo and english wording below the logo)
- - Product name: Coral Meadow Select Bird Nest
- - Some characteristic of 60% Indonesia (where the edible bird nest is harvested) and 40% Singapore (where the edible bird nest is sold). Maybe to incorporate some batik design or national flags
- - The chinese word for edible bird nest: 燕窩 (can be in the background)
- - The phrase: 100% Natural
- - The phrase: Harvested from pristine locations in Indonesia
- - Big transparent window to be able to see the product inside the box
- (pls see our competitor packaging 2 - attached)
- - Size of the sticker: width from left to right 15cm, height 12cm
Should not have
- - black color

```html
<!DOCTYPE html>
<html lang="en">
<head>
<meta charset="utf-8">
<title>Coral Meadow Select Bird Nest – Box Sticker</title>
<link rel="stylesheet" href="https://fonts.googleapis.com/css2?family=Almendra:wght@700&family=Cinzel:wght@700&family=Noto+Serif+TC:wght@700&display=swap">
<style>
  :root {
    --page: #f4f1ec;
    --red-deep: #b30f18;
    --red-bright: #e31c25;
    --gold: #f6d35a;
    --gold-soft: #d9883a;
    --window: #f3ece0;
  }
  html, body {
    margin: 0;
    width: 1200px;
    height: 1098px;
    overflow: hidden;
    background: var(--page);
  }
  .sticker {
    position: absolute;
    left: 30px;
    top: 93px;
    width: 1140px;
    height: 912px;
    border-radius: 22px;
    background: radial-gradient(ellipse at 50% 42%, var(--red-bright) 0%, #d4161f 45%, var(--red-deep) 100%);
    overflow: hidden;
  }
  .ornament {
    position: absolute;
    top: 20px;
    width: 240px;
    height: 390px;
    border-radius: 40px;
    background: radial-gradient(ellipse at center, rgba(217,136,58,0.35), rgba(217,136,58,0) 70%);
  }
  .ornament--left { left: 16px; }
  .ornament--right { right: 16px; }
  .brand-mark {
    position: absolute;
    left: 490px;
    top: 38px;
    width: 152px;
    height: 152px;
    box-sizing: border-box;
    border-radius: 50%;
    border: 8px solid var(--gold);
  }
  .brand-name {
    position: absolute;
    left: 0;
    right: 0;
    top: 210px;
    text-align: center;
    font-family: "Cinzel", serif;
    font-weight: 700;
    font-size: 29px;
    letter-spacing: 0.5px;
    color: var(--gold);
  }
  .product-name {
    position: absolute;
    left: 0;
    right: 0;
    top: 280px;
    margin: 0;
    text-align: center;
    font-family: "Almendra", serif;
    font-weight: 700;
    font-size: 74px;
    line-height: 1;
    color: var(--gold);
  }
  .window {
    position: absolute;
    left: 38px;
    top: 429px;
    width: 1064px;
    height: 381px;
    border-radius: 26px;
    background: var(--window);
  }
  .tab {
    position: absolute;
    left: 476px;
    width: 187px;
    background: var(--red-bright);
    color: var(--gold);
    text-align: center;
    box-sizing: border-box;
  }
  .tab--natural {
    top: 429px;
    height: 86px;
    border-radius: 0 0 14px 14px;
    padding-top: 10px;
    font-family: "Cinzel", serif;
    font-weight: 700;
    font-size: 25px;
    line-height: 34px;
  }
  .tab--hanzi {
    top: 736px;
    height: 76px;
    border-radius: 14px 14px 0 0;
    font-family: "Noto Serif TC", serif;
    font-weight: 700;
    font-size: 50px;
    line-height: 76px;
    letter-spacing: 2px;
    background: var(--red-deep);
  }
  .origin-line {
    position: absolute;
    left: 0;
    right: 0;
    top: 850px;
    text-align: center;
    font-family: "Cinzel", serif;
    font-weight: 700;
    font-size: 21px;
    letter-spacing: 2.6px;
    color: var(--gold);
  }
  .emblem {
    position: absolute;
    top: 838px;
    width: 78px;
    height: 52px;
    border-radius: 10px;
    background: radial-gradient(ellipse at center, rgba(217,136,58,0.45), rgba(217,136,58,0) 75%);
  }
  .emblem--lion { left: 46px; }
  .emblem--bird { right: 90px; }
</style>
</head>
<body>
  <div class="sticker">
    <div class="ornament ornament--left" role="img" aria-label="Gold batik floral vine ornament"></div>
    <div class="ornament ornament--right" role="img" aria-label="Gold batik floral vine ornament"></div>

    <div class="brand-mark"></div>
    <div class="brand-name">CORAL MEADOW</div>
    <h1 class="product-name">Select Bird Nest</h1>

    <div class="window" aria-label="Clear window showing the bird nests inside the box"></div>
    <div class="tab tab--natural">100%<br>NATURAL</div>
    <div class="tab tab--hanzi" lang="zh-Hant">燕窩</div>

    <div class="emblem emblem--lion" role="img" aria-label="Small batik-style lion illustration"></div>
    <div class="origin-line">HARVESTED FROM PRISTINE LOCATIONS IN INDONESIA</div>
    <div class="emblem emblem--bird" role="img" aria-label="Small batik-style swiftlet illustration"></div>
  </div>
</body>
</html>
```